The Quiet Harvest Plan Book Covers

Title: The Quiet Harvest Plan
Author: Milo Hartwell DC
Dimensions: 5 x 8 inches
Final Formats: JPG, PDF, PNG, AI/Vector + Layers/Fonts (Please send in zip folder and all must be at least 300 DPI)
FRONT AND BACK COVERS SEPARATE / NO SPINE

Description: Please take a look at the attached sketched photo as a demonstration of what I would like on the front cover. It should be books stacked on top of each other, the top one being the biggest and best book with the title on labeled above, on the spine of the book. The other books will be smaller and less meaningful, but please include the following titles for the books as shown in the picture: Ketogenic Diet, Low-Carb Diet, BRELLOW, PALEO Diet, and Grapefruit Diet.
Author's name should be on the bottom as shown. Please make the colors, clean, inviting and eye-catching. This will be a unisex book, so nothing too feminine (pinks, etc.), but definitely want it to pop.

Please contact me with any questions you have!

```html
<!DOCTYPE html>
<html lang="en">
<head>
<meta charset="utf-8">
<title>The Quiet Harvest Plan — Front Cover</title>
<link rel="stylesheet" href="https://fonts.googleapis.com/css2?family=Montserrat:wght@800;900&family=Roboto:wght@400;500;700&display=swap">
<style>
  :root {
    --stage: #e8e8e8;
    --paper: #f4f4f3;
    --paper-grain: #e6e6e4;
    --ink: #2f2f2f;
    --green: #6abf3a;
    --green-deep: #4fa22a;
    --spine-light: #fbfbfb;
    --spine-shade: #d9d9d9;
    --white: #ffffff;
  }
  * { margin: 0; padding: 0; box-sizing: border-box; }
  html, body { width: 1200px; height: 981px; overflow: hidden; }
  body { background: var(--stage); position: relative; font-family: "Roboto", Arial, sans-serif; }

  .cover {
    position: absolute; left: 319px; top: 40px;
    width: 562px; height: 900px; overflow: hidden;
    background: repeating-linear-gradient(90deg, var(--paper) 0 38px, var(--paper-grain) 38px 40px);
    box-shadow: 0 12px 30px rgba(0,0,0,.18);
  }
  .cover-photo {
    position: absolute; left: 0; top: 0; width: 100%; height: 96px;
    background: linear-gradient(90deg, #7bbf3e 0%, #cfe0b8 30%, #f3f1e6 55%, #f2c52a 72%, #b7d36a 92%);
  }
  .cover-title { position: absolute; left: 0; width: 100%; text-align: center; font-family: "Montserrat", Arial, sans-serif; }
  .title-lead { top: 112px; font-weight: 900; font-size: 40px; color: var(--ink); letter-spacing: -0.5px; }
  .title-main { top: 142px; font-weight: 900; font-size: 178px; line-height: 1; color: var(--green); letter-spacing: 2px; }

  .accent-disc {
    position: absolute; left: 110px; top: 420px; width: 720px; height: 720px;
    border-radius: 50%; background: var(--green);
  }
  .author-band { position: absolute; left: 0; bottom: 0; width: 100%; height: 130px; background: var(--green); }
  .author-rule { position: absolute; left: 110px; right: 110px; top: 30px; height: 2px; background: var(--white); opacity: .9; }
  .author-name { position: absolute; left: 0; width: 100%; top: 48px; text-align: center; color: var(--white); font-size: 19px; letter-spacing: .5px; }

  .spine-stack { position: absolute; left: 0; top: 340px; width: 100%; }
  .spine {
    position: absolute; height: 50px; display: flex; align-items: center; justify-content: center;
    background: linear-gradient(180deg, var(--spine-light) 0%, #efefef 55%, var(--spine-shade) 100%);
    border: 1px solid #cfcfcf; box-shadow: 0 3px 6px rgba(0,0,0,.22);
    font-size: 22px; color: var(--ink);
  }
  .spine--green { color: var(--green-deep); }
  .spine--hero { font-weight: 700; font-size: 25px; color: var(--green-deep); }
</style>
</head>
<body>
  <main class="cover">
    <div class="cover-photo" role="img" aria-label="Fresh vegetables on a white wooden table: lettuce, corn and avocado"></div>
    <h1>
      <span class="cover-title title-lead">THE QUIET HARVEST</span>
      <span class="cover-title title-main">PLAN</span>
    </h1>
    <div class="accent-disc"></div>

    <section class="spine-stack" aria-label="Stacked book spines">
      <div class="spine spine--hero" style="left:70px;width:400px;top:0;transform:rotate(-2deg);">The Quiet Harvest Plan</div>
      <div class="spine" style="left:90px;width:330px;top:52px;transform:rotate(-2.5deg);">Ketogenic Diet</div>
      <div class="spine spine--green" style="left:100px;width:390px;top:104px;transform:rotate(-3deg);">Low-Carb Diet</div>
      <div class="spine" style="left:60px;width:420px;top:158px;transform:rotate(-4deg);">BRELLOW</div>
      <div class="spine spine--green" style="left:110px;width:410px;top:212px;transform:rotate(-3.5deg);">PALEO Diet</div>
      <div class="spine" style="left:120px;width:400px;top:266px;transform:rotate(-2.5deg);">Grapefruit Diet</div>
    </section>

    <footer class="author-band">
      <div class="author-rule"></div>
      <p class="author-name">By: Milo Hartwell DC</p>
    </footer>
  </main>
</body>
</html>
```